Word Page Templates x 5

1 x Letterhead Template with Header and Footer able to be printed to paper and pdf with non blurry resolution
- File attached looks ok on computer screen but does not print the same
- We are wanting it to print like it looks on the screen
- We are wanting it to print not fuzzy in resolution
- We are wanting the banner to be on the absolute edge of the page like it is on the computer screen
- We are needing to print this to paper and pdf with perfect resolution and colour

Please can someone help us!!

I have provided the logo files in our posession. If better resolutions are required please let us know.

We are also wanting 4 simple page templates to be setup in Landscape and Portrait orientation as well once we are happy with the letterhead that is provided samples have been provided
Updates

Hi all I have the vector files available now along with a Colour profile

Requirements
Must have
• Clear when printed on A4 Paper
Should not have
• Blurry images, Colour must be correct (same as Logo) - Please reference our website if need be ..... vornal.com.au

```html
<!DOCTYPE html>
<html lang="en">
<head>
<meta charset="utf-8">
<title>Vornal Pavement Services – Letterhead</title>
<link rel="stylesheet" href="https://fonts.googleapis.com/css2?family=Montserrat:wght@800&display=swap">
<style>
  :root {
    --brand-green: #00843f;
    --brand-navy: #283a7e;
    --paper: #ffffff;
    --page-w: 1200px;
    --page-h: 848px;
    --band-h: 36px;
  }
  * { margin: 0; padding: 0; box-sizing: border-box; }
  html, body {
    width: var(--page-w);
    height: var(--page-h);
    overflow: hidden;
    background: var(--paper);
  }
  .letterhead {
    position: relative;
    width: var(--page-w);
    height: var(--page-h);
    background: var(--paper);
  }
  .edge-band {
    position: absolute;
    left: 0;
    width: 100%;
    height: var(--band-h);
    background: linear-gradient(90deg, var(--brand-green) 0%, var(--brand-navy) 100%);
  }
  .edge-band--top { top: 0; }
  .edge-band--bottom { bottom: 0; }
  .brand-name {
    position: absolute;
    right: 33px;
    top: 722px;
    text-align: right;
    font-family: 'Montserrat', sans-serif;
    font-weight: 800;
    color: var(--brand-navy);
    line-height: 1;
  }
  .brand-name__main {
    display: block;
    font-size: 58px;
    letter-spacing: 2px;
  }
  .brand-name__sub {
    display: block;
    margin-top: 8px;
    font-size: 13.5px;
    letter-spacing: 1.6px;
  }
</style>
</head>
<body>
  <main class="letterhead">
    <div class="edge-band edge-band--top" role="img" aria-label="Header band with green-to-navy gradient and white chevron stripe"></div>

    <div class="brand-name">
      <span class="brand-name__main">VORNAL</span>
      <span class="brand-name__sub">PAVEMENT SERVICES</span>
    </div>

    <div class="edge-band edge-band--bottom" role="img" aria-label="Footer band with green-to-navy gradient and white chevron stripe"></div>
  </main>
</body>
</html>
```